Adult Literacy Program - flyer to attract volunteers and students

We want a flyer that is engaging, colorful, modern and will appeal to our primary audience of adults aged 40-60. We are trying to attract both prospective volunteers (typically age 50+, mostly women) and students (typically aged 40+).
The flyer should feature diverse people working together in pairs of two, reading or talking, with a workbook or some reading material in front of them.

Our organization trains tutors to work one-on-one with adults who are learning how to read. Most of our adult students are non-native speakers of English. Many are of Haitian or Hispanic origin, so we would like some people who represent that demographic.

The Flyer should represent reading, learning, literacy, knowledge, growth,
and opportunities.
Our students are learning to read so they can advance their job opportunities.

Target Market(s)

Adults aged 40-60, primarily women, retired, volunteers

Industry/Entity Type

Education

Font styles to use
Serif
Sans Serif

Colors

Designer to choose colors to be used in the design.

Requirements
Must have
• - UPDATE: Should be designed as a TRI-FOLD brochure on 8.5 x 11 inch paper that will be folded into thirds.
• - Images of diverse people, women and men, who look Hispanic, Haitian and other nationalities as well as Caucasian.
• - Our logo on the front cover
Nice to have
• The sample flyer is very boring and dry! We are open to different ways of presenting the text.

```html
<!DOCTYPE html>
<html lang="en">
<head>
<meta charset="utf-8">
<title>Reading Bridge Partners – Tri-fold Brochure</title>
<link href="https://fonts.googleapis.com/css2?family=Open+Sans:wght@400;600;700;800&display=swap" rel="stylesheet">
<style>
:root{
  --navy:#0c2668;
  --blue:#163f99;
  --sky:#2a9fdc;
  --paper:#ffffff;
  --panel-grey:#e9eaec;
  --ink:#0c2668;
  --text-dark:#1f2a44;
  --backdrop:#2e2e30;
  --photo-warm-1:#c9a98a;
  --photo-warm-2:#7d6a5a;
  --photo-cool-1:#9fb3c9;
  --photo-cool-2:#5c6f86;
}
*{box-sizing:border-box;margin:0;padding:0}
html,body{width:800px;height:1200px;overflow:hidden}
body{background:var(--backdrop);font-family:"Open Sans",Arial,sans-serif;position:relative}
.sheet{position:absolute;left:40px;width:720px;height:556px;display:flex;background:var(--paper);box-shadow:0 8px 24px rgba(0,0,0,.5)}
.sheet::after{content:"";position:absolute;left:0;right:0;bottom:0;height:6px;background:var(--sky)}
.sheet--outside{top:22px}
.sheet--inside{top:622px}
.panel{position:relative;width:240px;height:100%;overflow:hidden}
.panel + .panel{border-left:1px solid rgba(0,0,0,.08)}
.photo{position:absolute;left:0;right:0}
.checklist{list-style:none}
.checklist li{position:relative;padding-left:16px;line-height:1.3;margin-bottom:3px}
.checklist li svg{position:absolute;left:0;top:3px;width:10px;height:10px}

/* Tutors panel */
.tutors{background:var(--paper)}
.tutors__blue{position:absolute;top:0;left:0;right:0;height:350px;background:linear-gradient(180deg,var(--blue),var(--navy));color:#fff;padding:56px 20px 0 22px}
.tutors h2{font-size:19px;font-weight:700;letter-spacing:.5px;margin-bottom:8px}
.tutors .checklist{font-size:10.5px}
.tutors__slogan{margin-top:20px;font-size:19px;line-height:1.12;text-transform:uppercase}
.tutors__slogan b{font-weight:800}
.tutors__slogan span{font-weight:400}
.tutors .photo{top:350px;bottom:6px;background:linear-gradient(135deg,var(--photo-warm-1),var(--photo-warm-2))}

/* Contact panel */
.contact{background:linear-gradient(160deg,#f4f4f5,var(--panel-grey));text-align:center;color:var(--ink);padding-top:118px}
.brand{font-weight:700;color:var(--sky);font-size:15px;letter-spacing:.5px;line-height:1.2;display:flex;align-items:center;justify-content:center;gap:6px}
.brand i{display:inline-block;width:10px;height:10px;border-radius:50%;background:var(--sky)}
.contact h2{margin-top:24px;font-size:19px;font-weight:800;line-height:1.05}
.contact h2 span{display:block;font-size:15px;font-weight:700}
.contact__lead{margin-top:14px;font-size:11px;font-weight:700;line-height:1.3}
.contact__lead span{font-weight:400;display:block}
.contact__list{list-style:none;margin-top:10px;font-size:10.5px;font-weight:600;line-height:1.35}
.contact__list li{margin-bottom:5px}
.contact__list svg{width:10px;height:10px;vertical-align:-1px;margin-right:4px}
.partner{position:absolute;left:0;right:0;bottom:40px;display:flex;justify-content:center;align-items:center;gap:6px;font-size:11px;font-weight:700;color:var(--ink)}
.partner i{width:14px;height:14px;background:#f2c92b;border-radius:50%;display:inline-block}

/* Cover panel */
.cover{background:var(--paper)}
.cover__tab{position:absolute;top:0;left:0;right:0;height:44px;background:var(--blue);color:#fff;font-weight:800;font-size:21px;letter-spacing:.5px;padding:10px 0 0 30px;z-index:2}
.cover .photo{top:44px;height:250px;background:linear-gradient(135deg,var(--photo-cool-1),var(--photo-warm-2))}
.cover__band{position:absolute;top:280px;left:0;right:0;height:84px;background:var(--navy);color:#fff;text-align:center;padding-top:14px}
.cover__band h1{font-size:21px;font-weight:800;letter-spacing:.3px}
.cover__band p{font-size:10.5px;line-height:1.3;margin-top:4px}
.cover__band p b{font-weight:800}
.cover .brand{position:absolute;left:0;right:0;top:430px}

/* Students panel */
.students{padding:40px 18px 0 22px;color:var(--text-dark)}
.students h2{font-size:19px;font-weight:700;color:var(--ink);margin-bottom:8px}
.students__intro{font-size:10.5px;font-weight:700;margin-bottom:3px}
.students .checklist{font-size:10.5px}
.students .checklist--sub li{font-weight:400}
.students .checklist--bold li{font-weight:700}
.students__tag{margin-top:14px;font-size:16px;color:var(--ink);line-height:1.1}
.students__tag b{display:block;font-size:19px;font-weight:800}
.students .photo{top:372px;bottom:6px;background:linear-gradient(135deg,var(--photo-warm-1),#8e7b6a)}

/* Inside info panels */
.info .photo{top:0;height:330px}
.info--about .photo{background:linear-gradient(135deg,var(--photo-warm-1),#9a8574)}
.info--why .photo{background:linear-gradient(135deg,#b8c3cf,var(--photo-warm-2));height:300px}
.info__blue{position:absolute;left:0;right:0;bottom:0;background:linear-gradient(180deg,var(--blue),var(--navy));color:#fff;padding:40px 20px 0 24px}
.info--about .info__blue{top:310px;clip-path:polygon(0 20px,100% 0,100% 100%,0 100%)}
.info--why .info__blue{top:280px;clip-path:polygon(0 20px,100% 0,100% 100%,0 100%)}
.info h2{font-size:18px;font-weight:700;margin-bottom:10px}
.info p{font-size:10px;line-height:1.45}
</style>
</head>
<body>

<svg width="0" height="0" style="position:absolute" aria-hidden="true">
  <defs>
    <symbol id="tick" viewBox="0 0 10 10"><path d="M1 5.5 L4 8.5 L9 1.5" fill="none" stroke="currentColor" stroke-width="1.8" stroke-linecap="round" stroke-linejoin="round"/></symbol>
    <symbol id="phone" viewBox="0 0 10 10"><circle cx="5" cy="5" r="4.3" fill="none" stroke="currentColor" stroke-width="1"/><path d="M3.3 2.8 L4.2 2.6 L4.6 3.8 L4 4.3 Q4.6 5.6 5.7 6 L6.2 5.4 L7.4 5.8 L7.2 6.7 Q4 7 3.3 2.8Z" fill="currentColor"/></symbol>
    <symbol id="pin" viewBox="0 0 10 10"><path d="M5 9.5 L2 5 A3.3 3.3 0 1 1 8 5 Z" fill="currentColor"/><circle cx="5" cy="3.8" r="1.2" fill="#fff"/></symbol>
    <symbol id="mail" viewBox="0 0 10 10"><rect x="0.8" y="2" width="8.4" height="6" fill="none" stroke="currentColor" stroke-width="1"/><path d="M0.8 2 L5 5.5 L9.2 2" fill="none" stroke="currentColor" stroke-width="1"/></symbol>
  </defs>
</svg>

<!-- Outside spread -->
<section class="sheet sheet--outside">
  <article class="panel tutors">
    <div class="tutors__blue">
      <h2>TUTORS</h2>
      <ul class="checklist">
        <li><svg><use href="#tick"/></svg>No special skills or degrees needed — just a degree of caring!</li>
        <li><svg><use href="#tick"/></svg>Training offered throughout the year</li>
        <li><svg><use href="#tick"/></svg>Tutors meet students weekly at a library</li>
        <li><svg><use href="#tick"/></svg>Instructional materials provided</li>
        <li><svg><use href="#tick"/></svg>Ongoing support available</li>
      </ul>
      <p class="tutors__slogan"><b>Teach an adult</b><br><span>to read and</span><br><b>you'll change<br>a life forever</b></p>
    </div>
    <div class="photo" role="img" aria-label="Smiling woman tutoring at a library table with adult learners behind her"></div>
  </article>

  <article class="panel contact">
    <div class="brand"><i></i>READING BRIDGE<br>PARTNERS</div>
    <h2>DON'T WASTE<span>A MOMENT!</span></h2>
    <p class="contact__lead">Contact us today<span>to learn more.</span>Volunteer Desk</p>
    <ul class="contact__list">
      <li><svg><use href="#phone"/></svg>555-204-7510</li>
      <li><svg><use href="#pin"/></svg>Millbrook, Ashford<br>&amp; South Vale</li>
      <li><svg><use href="#phone"/></svg>555-310-3453</li>
      <li><svg><use href="#mail"/></svg>literacy@lakeshorelib.org</li>
    </ul>
    <div class="partner"><i></i>Lakeshore County Library</div>
  </article>

  <article class="panel cover">
    <div class="cover__tab">VOLUNTEER</div>
    <div class="photo" role="img" aria-label="Older man and younger woman reading together at a library table"></div>
    <div class="cover__band">
      <h1>ENRICH A LIFE!</h1>
      <p>HELP AN ADULT LEARN TO READ<br><b>WRITE OR SPEAK ENGLISH</b></p>
    </div>
    <div class="brand"><i></i>READING BRIDGE<br>PARTNERS</div>
  </article>
</section>

<!-- Inside spread -->
<section class="sheet sheet--inside">
  <article class="panel students">
    <h2>STUDENTS</h2>
    <p class="students__intro">Students are adults in need of</p>
    <ul class="checklist checklist--sub">
      <li><svg><use href="#tick"/></svg>basic literacy skills</li>
      <li><svg><use href="#tick"/></svg>pre-GED skills</li>
      <li><svg><use href="#tick"/></svg>conversational English</li>
    </ul>
    <ul class="checklist checklist--bold">
      <li><svg><use href="#tick"/></svg>Tutoring is free of charge</li>
      <li><svg><use href="#tick"/></svg>Tutoring is one-on-one</li>
      <li><svg><use href="#tick"/></svg>Flexible scheduling during library hours</li>
      <li><svg><use href="#tick"/></svg>Lessons focus on student goals</li>
    </ul>
    <p class="students__tag">IF YOU CAN READ,<b>YOU CAN TUTOR!</b></p>
    <div class="photo" role="img" aria-label="Two women reading a workbook together at a library desk"></div>
  </article>

  <article class="panel info info--about">
    <div class="photo" role="img" aria-label="Smiling woman holding a book while talking with a tutor"></div>
    <div class="info__blue">
      <h2>ABOUT US</h2>
      <p>Lorem ipsum dolor sit amet, consectetur adipiscing elit, sed do eiusmod tempor incididunt ut labore et dolore magna aliqua. Ut enim ad minim veniam, quis nostrud exercitation ullamco laboris nisi ut aliquip ex ea commodo consequat. Duis aute irure dolor in reprehenderit in voluptate velit esse cillum dolore eu fugiat nulla pariatur.</p>
    </div>
  </article>

  <article class="panel info info--why">
    <div class="photo" role="img" aria-label="Diverse adult learners and tutors studying together in a library"></div>
    <div class="info__blue">
      <h2>WHY CHOOSE US</h2>
      <p>Lorem ipsum dolor sit amet, consectetur adipiscing elit, sed do eiusmod tempor incididunt ut labore et dolore magna aliqua. Ut enim ad minim veniam, quis nostrud exercitation ullamco laboris nisi ut aliquip ex ea commodo consequat. Duis aute irure dolor in reprehenderit in voluptate velit esse cillum dolore eu fugiat nulla pariatur.</p>
    </div>
  </article>
</section>

</body>
</html>
```